Ansprechendes Layout für Geschichte von Oldtimern
Grossartiges Design, supernette Zusammenarbeit, megaschnelle Rückmeldung auf meine dusseligen Fragen - dass "Marvin Stelle" sich meines Projektes angenommen hat, war ein echter Glückstreffer! Ich bin sowohl mit dem Ergebnis als auch mit der Kommunikation während des gesamten Prozesses absolut happy! Das hat richtig Spaß gemacht und auf meine Oldtimer-"Broschüre" bin ich stolz wie Bolle... Schade, dass man hier nicht 10 Sterne vergeben kann - "Marvin Stelle" hätte sie verdient!
Zielgruppe
Ich mache mich aktuell selbstständig als Solo-Freiberuflerin (Redakteurin) mit dem Projekt 'Das Wagen-Tagebuch': Ich schreibe für Oldtimer-Besitzer die Lebensgeschichte ihres Oldtimers auf - lebendig und augenzwinkernd. Zielgruppe: Oldtimer-Besitzer, die die Historie ihres Wagens als individuelles 'Buch' haben möchten; für sich selbst oder auch als Verkaufsargument beim Weiterverkauf des Oldtimers.
Aufgabenstellung
Mein Text wird auf hochwertigem Papier (einseitig) gedruckt , im Format A4 quer. Ein paar gut platzierte Fotos sollen den Text 'auflockern'. Für dieses Layout von Titelseite sowie Text & Fotos suche ein 'hinreißendes' Design (Schriften und Layout). Die fertigen Seiten werden dann in einer Druckerei ausgedruckt und in einen A4 Querformat-Klemmbinder 'reingesteckt'. Deswegen muss links entsprechend viel Rand/Platz gelassen werden. Wichtig ist mir eine sehr edle und hochwertige Anmutung des Layouts. Es soll kein 'Bildband' werden, die Fotos ergänzen lediglich den Text, der 'im Mittelpunkt' steht.

```html
<!DOCTYPE html>
<html lang="de">
<head>
<meta charset="utf-8">
<title>Das Wagen-Tagebuch – Seiten</title>
<link href="https://fonts.googleapis.com/css2?family=Carlito&family=Fira+Sans:wght@400&family=Fira+Sans+Condensed:wght@400&display=swap" rel="stylesheet">
<style>
  :root {
    --gold: #b8a25c;
    --charcoal: #333333;
    --ink: #1e1e1e;
    --paper: #ffffff;
    --canvas: #ffffff;
    --photo-dark: #1d2420;
    --photo-mid: #3a4a3c;
  }
  * { margin: 0; padding: 0; box-sizing: border-box; }
  html, body { width: 1200px; height: 2554px; overflow: hidden; background: var(--canvas); }
  .page {
    position: absolute; left: 88px; width: 1035px; height: 732px;
    background: var(--paper);
    box-shadow: 2px 3px 4px rgba(0,0,0,0.18);
  }
  .page--1 { top: 148px; }
  .page--2 { top: 921px; }
  .page--3 { top: 1689px; }
  .page__top-rule { position: absolute; left: 0; top: 0; width: 100%; height: 6px; background: var(--charcoal); }
  .page__gold-rule { position: absolute; left: 0; top: 685px; width: 100%; height: 6px; background: var(--gold); }
  .page__foot-band { position: absolute; left: 0; top: 698px; width: 100%; height: 34px; background: var(--charcoal); }
  .brand { position: absolute; left: 672px; top: 44px; width: 293px; text-align: right; }
  .brand__name {
    font-family: "Fira Sans", sans-serif; font-weight: 400;
    color: var(--gold); font-size: 30px; line-height: 1.1;
  }
  .brand__mark { display: inline-block; width: 12px; height: 12px; background: var(--gold); margin-right: 8px; vertical-align: middle; }
  .brand__tagline {
    margin-top: 12px; font-family: "Fira Sans Condensed", sans-serif;
    color: var(--charcoal); font-size: 13px; letter-spacing: 0.4px;
  }
  .photo { position: absolute; left: 173px; width: 353px; }
  .photo--front { top: 256px; height: 235px; background: linear-gradient(160deg, var(--photo-mid), var(--photo-dark) 60%, #2a2a2a); }
  .photo--side { top: 257px; height: 217px; background: linear-gradient(170deg, #3f5a3a 0%, #2b3a30 45%, #1c2230 70%, #8a8a86 100%); }
  .copy {
    position: absolute; width: 374px;
    font-family: "Carlito", "Calibri", sans-serif; font-size: 13.3px; line-height: 18.45px;
    letter-spacing: 0.15px;
    color: var(--ink); text-align: justify;
  }
  .copy--right { left: 565px; top: 255px; }
  .copy--col-a { left: 173px; top: 255px; width: 365px; }
  .copy--col-b { left: 575px; top: 255px; width: 364px; }
</style>
</head>
<body>

<section class="page page--1">
  <div class="page__top-rule"></div>
  <header class="brand">
    <div class="brand__name"><span class="brand__mark"></span>Das Wagen-Tagebuch</div>
    <div class="brand__tagline">Erinnerungen auf vier Rädern</div>
  </header>
  <div class="photo photo--front" role="img" aria-label="Foto: dunkler Oldtimer-Sedan von vorn vor grüner Hecke"></div>
  <p class="copy copy--right">Lass mich mal eben nachrechnen: Wie alt war ich eigentlich damals, 1993? Ja, jetzt hab‘ ich’s: 26! Grandioses Auto-Alter, wenn Du mich fragst. Man ist erfahren, gelassen, souverän. Wissbegierig und neugierig war ich sowieso schon immer: Interessiert habe ich stets die Ohren gespitzt, wenn meine Fahrgäste über die aktuelle Politik oder die allgemeine Wirtschaftslage diskutiert haben. 1993 beherrschte gerade der Vertrag von Maastricht, mit dem die Europäische Union erstmals Wirklichkeit wurde, die Berichterstattung in allen Gazetten. Das bot natürlich reichlich Zündstoff für Diskussionen. Da ging es manchmal ganz schön hoch her, wenn Fahrer und Beifahrer über das Pro und Contra philosophierten… Ach, und dann war doch damals im Januar auch noch der Amtsantritt des neuen amerikanischen Präsidenten Will Clanton. Das war doch der, der später dann mit seiner Praktikantin…? Na, Du weißt schon…</p>
  <div class="page__gold-rule"></div>
  <div class="page__foot-band"></div>
</section>

<section class="page page--2">
  <div class="page__top-rule"></div>
  <header class="brand">
    <div class="brand__name"><span class="brand__mark"></span>Das Wagen-Tagebuch</div>
    <div class="brand__tagline">Erinnerungen auf vier Rädern</div>
  </header>
  <p class="copy copy--col-a">Nur um das an dieser Stelle gleich mal klarzustellen: Ich war natürlich niemals ein schnödes Taxi. Nix da mit Fahrten für Jedermann! Ich war in meinem ersten Leben ein ganz besonderer Dienstwagen – nämlich der Direktionswagen vom Nähmaschinen-Handel Falkner! Mit piekfeiner Firmenadresse, wie sich das gehört: Hamburg, Lindenallee 1. Jawohl! Mit standesgemäßer Sonderausstattung: elegantes Elfenbein-Lenkrad! Kuschelige Schlummerrolle für die Frau auf der Beifahrerseite! Hochwertiges Bergner-Mexiko-Radio! Stolze 95 PS! Und natürlich das gesamte Sicherheitspaket. 8.665 Mark musste Nähmaschinen Falkner 1967, als ich unter der Bezeichnung Modell K7 als sogenannte „Kleine Schwinge“ gebaut wurde, auf den Tisch legen. Kennst Du dieses Unternehmen eigentlich heutzutage noch? Das war ja eine ganz große Nummer damals! Gegründet wurde Nähmaschinen Falkner</p>
  <p class="copy copy--col-b">1862 von einem gewissen Georg Michael Falkner. Der war eigentlich Instrumentenmacher, sattelte dann aber um und baute sein Unternehmen zu einem der Marktführer in Sachen Nähmaschinen auf. Gleichzeitig war er sehr sozial eingestellt und führte eine Krankenunterstützungskasse sowie kurz darauf auch eine Rentenkasse ein. Schon bald exportierte die Firma ihre Nähmaschinen in die ganze Welt; 1936 wurde bereits die dreimillionste Maschine hergestellt. Und ausgerechnet in dem Jahr, in dem ich vom Band lief, führte das Unternehmen die allererste Zick-Zack-Nähmaschine ein – mit 6.000 Stichen pro Minute! Goldene Zeiten waren das für Falkner, auch für mich in Hamburg. Leider ist von dem damaligen Glanz und der einstigen Größe nicht mehr viel übriggeblieben: Heute ist das Unternehmen in chinesischer Hand. Aber wir wollen ja jetzt nicht sentimental werden…</p>
  <div class="page__gold-rule"></div>
  <div class="page__foot-band"></div>
</section>

<section class="page page--3">
  <div class="page__top-rule"></div>
  <header class="brand">
    <div class="brand__name"><span class="brand__mark"></span>Das Wagen-Tagebuch</div>
    <div class="brand__tagline">Erinnerungen auf vier Rädern</div>
  </header>
  <div class="photo photo--side" role="img" aria-label="Foto: dunkelblauer Oldtimer-Sedan schräg von der Seite vor Bäumen"></div>
  <p class="copy copy--right">Wusstest Du übrigens, dass in meinem Geburtsjahr 1967 das Benzin gerade mal 59 Pfennige und Diesel 56 Pfennige pro Liter kostete? Nur mal, so zum Vergleich: Heute, im Jahr 2021, zahlt man an der Tankstelle für einen Liter Super knapp 1,50 Euro, und für den Liter Diesel knapp 1,30 Euro! Rechne diese Preissteigerung jetzt bloß nicht noch in DM um… Ach, es waren einfach ganz andere Zeiten damals: Unser Bundeskanzler hieß Kurt Georg Kessler, Eintracht Brunsberg wurde Deutscher Fußballmeister, die jungen Damen trugen bevorzugt verwegen kurze Miniröcke, und wenn man mein Radio anschaltete, gab’s tolle Musik von den Doorways, den Rolling Pebbles oder auch von Reinhold Meier, der damals gerade sein erstes Album veröffentlichte. Ganz schön lange her das alles, aber ich erinnere mich daran, als ob es erst gestern gewesen wäre… Aber ich schweife wohl etwas ab…</p>
  <div class="page__gold-rule"></div>
  <div class="page__foot-band"></div>
</section>

</body>
</html>
```